" O Tavelune.com é uma startup voltada para a organizaçao de eventos. Com um novo modelo de negócio através de nossa ferramenta o usuário poderá contratar, solicitar orçamentos e conversar através de chat com várias empresas e assim fechar negócio com o empresa que mais se ajusta a realidade financeira dele. Em nossa ferramenta teremos cadastrados fotógrafos, buffet, decoradores, maquiadores e etc... Todas as empresas e profissionais que estao envolvidas na organizaçao de um evento. "

```html
<!DOCTYPE html>
<html lang="pt-BR">
<head>
<meta charset="utf-8">
<title>Tavelune.com — Cartão de visita</title>
<link rel="stylesheet" href="https://fonts.googleapis.com/css2?family=Roboto:wght@400;700&display=swap">
<style>
  :root {
    --backdrop: #d9d9d9;
    --card-white: #ffffff;
    --card-black: #151515;
    --ink: #1a1a1a;
    --ink-soft: #333333;
    --gold: #e3a63a;
  }
  * { margin: 0; padding: 0; box-sizing: border-box; }
  html, body {
    width: 1200px;
    height: 1200px;
    overflow: hidden;
    background: var(--backdrop);
    font-family: "Roboto", Arial, sans-serif;
  }
  .sheet {
    position: relative;
    width: 1200px;
    height: 1200px;
  }
  .card {
    position: absolute;
    left: 180px;
    width: 840px;
    height: 480px;
    border-radius: 4px;
    box-shadow: 0 10px 30px rgba(0,0,0,0.18);
    overflow: hidden;
  }
  .card--front { top: 90px; background: var(--card-white); color: var(--ink); }
  .card--back { top: 630px; background: var(--card-black); }

  .brand {
    display: flex;
    align-items: center;
    gap: 12px;
    font-weight: 700;
    white-space: nowrap;
  }
  .brand__mark {
    display: inline-block;
    border-radius: 6px;
  }
  .card--front .brand {
    position: absolute;
    left: 60px;
    top: 205px;
    font-size: 52px;
    color: var(--ink);
  }
  .card--front .brand__mark { width: 40px; height: 40px; background: var(--ink); }

  .holder {
    position: absolute;
    left: 470px;
    top: 78px;
  }
  .holder__name { font-size: 30px; font-weight: 700; }
  .holder__role { font-size: 13px; color: var(--ink-soft); margin-top: 4px; margin-left: 120px; }

  .contact {
    position: absolute;
    left: 555px;
    top: 200px;
    font-size: 17px;
    line-height: 1.35;
    color: var(--ink);
  }
  .contact__email { font-size: 13px; margin-top: 4px; }

  .address {
    position: absolute;
    left: 560px;
    top: 335px;
    font-size: 14px;
    line-height: 1.4;
    color: var(--ink);
  }

  .pattern {
    position: absolute;
    inset: 0;
    background: radial-gradient(ellipse at 50% 45%, #1f1f1f 0%, var(--card-black) 70%);
  }
  .card--back .brand {
    position: absolute;
    left: 50%;
    top: 50%;
    transform: translate(-50%, -50%);
    font-size: 64px;
    color: var(--gold);
  }
  .card--back .brand__mark { width: 50px; height: 50px; background: var(--gold); }
</style>
</head>
<body>
  <main class="sheet">
    <section class="card card--front" aria-label="Frente do cartão">
      <div class="brand"><span class="brand__name">Tavelune.com</span><span class="brand__mark"></span></div>
      <div class="holder">
        <p class="holder__name">Marina Solano</p>
        <p class="holder__role">CEO &amp; Founder</p>
      </div>
      <div class="contact">
        <p>(94) 5550-1234</p>
        <p>(91) 5550-8765</p>
        <p class="contact__email">marinasolano@tavelune.com</p>
      </div>
      <div class="address">
        <p>Rua das Acácias, 210</p>
        <p>Jardim Aurora, Vilarejo/PA</p>
      </div>
    </section>

    <section class="card card--back" aria-label="Verso do cartão">
      <div class="pattern" role="img" aria-label="Padrão discreto de ícones de eventos em tons de cinza escuro"></div>
      <div class="brand"><span class="brand__name">Tavelune.com</span><span class="brand__mark"></span></div>
    </section>
  </main>
</body>
</html>
```